New Business Card Design Project

We would like a business card that represents the sale of boat, home, auto, and life insurance.

The logo can change colors to meet the look of the design if needed.

Industry/Entity Type

Business

```html
<!DOCTYPE html>
<html lang="en">
<head>
<meta charset="utf-8">
<title>Keelway Financial – Business Card</title>
<link href="https://fonts.googleapis.com/css2?family=Jost:wght@400;500&family=Open+Sans:wght@400;600;700&display=swap" rel="stylesheet">
<style>
  :root {
    --stage: #e4e2df;
    --card-black: #0d0e10;
    --card-white: #ffffff;
    --brand-blue: #2e86a8;
    --ink: #1c1c1c;
    --ink-soft: #333333;
    --photo-dark: #2a2422;
    --photo-mid: #8a6a58;
    --photo-light: #f4f1ee;
  }
  * { box-sizing: border-box; margin: 0; padding: 0; }
  html, body { width: 1200px; height: 768px; overflow: hidden; }
  body {
    background: var(--stage);
    position: relative;
    font-family: "Open Sans", Arial, sans-serif;
  }
  .card {
    position: absolute;
    top: 234px;
    width: 520px;
    height: 300px;
    overflow: hidden;
  }
  /* Front */
  .card-front {
    left: 50px;
    background: var(--card-black);
    display: flex;
    flex-direction: column;
    align-items: center;
    justify-content: center;
    gap: 10px;
  }
  .brand-name {
    font-family: "Jost", "Futura", sans-serif;
    font-weight: 500;
    font-size: 40px;
    letter-spacing: 3px;
    color: var(--card-white);
  }
  .brand-tagline {
    font-family: "Jost", "Futura", sans-serif;
    font-weight: 400;
    font-size: 19px;
    letter-spacing: 1.5px;
    color: var(--card-white);
  }
  /* Back */
  .card-back {
    left: 630px;
    background: var(--card-white);
  }
  .portrait {
    position: absolute;
    left: 0;
    top: 55px;
    width: 255px;
    height: 215px;
    background: linear-gradient(180deg, var(--photo-light) 0%, var(--photo-mid) 35%, var(--photo-dark) 60%, var(--card-black) 100%);
    border-radius: 110px 110px 0 0;
  }
  .card-bands {
    position: absolute;
    left: 0;
    top: 0;
  }
  .contact-block {
    position: absolute;
    right: 24px;
    top: 78px;
    text-align: right;
    color: var(--ink);
  }
  .person-name {
    font-weight: 700;
    font-size: 17px;
    color: var(--brand-blue);
  }
  .person-title {
    font-size: 12px;
    color: var(--ink-soft);
    margin-top: 2px;
  }
  .contact-list {
    list-style: none;
    margin-top: 16px;
    font-size: 12.5px;
    line-height: 19px;
  }
  .contact-list li {
    display: flex;
    justify-content: flex-end;
    align-items: center;
    gap: 8px;
  }
  .contact-icon { width: 12px; height: 12px; flex: none; }
  .contact-address {
    margin-top: 4px;
    font-size: 12.5px;
    line-height: 18px;
    padding-right: 20px;
  }
</style>
</head>
<body>
  <section class="card card-front" aria-label="Card front">
    <div class="brand-name">KEELWAY FINANCIAL</div>
    <div class="brand-tagline">investments &amp; insurance</div>
  </section>

  <section class="card card-back" aria-label="Card back">
    <div class="portrait" role="img" aria-label="Portrait photo of the agent in a dark shirt and tie"></div>
    <svg class="card-bands" width="520" height="300" viewBox="0 0 520 300" aria-hidden="true">
      <polygon points="0,262 250,262 262,282 0,282" fill="var(--brand-blue)"/>
      <polygon points="248,270 520,270 520,300 0,300 0,282 262,282" fill="var(--card-black)"/>
      <polygon points="250,262 258,262 270,278 262,282" fill="var(--card-white)"/>
    </svg>

    <div class="contact-block">
      <div class="person-name">Your Long Name</div>
      <div class="person-title">Your Title</div>
      <ul class="contact-list">
        <li>000 0 0 000 00
          <svg class="contact-icon" viewBox="0 0 12 12"><path d="M1 4 Q6 0 11 4 L9 5 L8 4 Q6 3 4 4 L3 5 Z M3 6 H9 L10 11 H2 Z" fill="var(--brand-blue)"/></svg></li>
        <li>(00) 0 0 0000 0000
          <svg class="contact-icon" viewBox="0 0 12 12"><rect x="3" y="1" width="6" height="4" fill="none" stroke="var(--brand-blue)"/><rect x="1" y="5" width="10" height="6" fill="var(--brand-blue)"/></svg></li>
        <li>yourname@yourwebsite.com
          <svg class="contact-icon" viewBox="0 0 12 12"><rect x="1" y="2.5" width="10" height="7" fill="var(--brand-blue)"/><path d="M1 2.5 L6 7 L11 2.5" fill="none" stroke="#fff"/></svg></li>
        <li>www.yourwebsite.com
          <svg class="contact-icon" viewBox="0 0 12 12"><circle cx="6" cy="6" r="5" fill="none" stroke="var(--brand-blue)" stroke-width="1.4"/><path d="M1 6 H11 M6 1 V11 M6 1 Q2 6 6 11 M6 1 Q10 6 6 11" fill="none" stroke="var(--brand-blue)" stroke-width="0.9"/></svg></li>
      </ul>
      <p class="contact-address">Your office or residentianal address<br>in just two line with pin code.</p>
    </div>
  </section>
</body>
</html>
```